marcello's mobile mechanic

a business card that will get attention from clients
- name of the business: M'S MOBILE MECHANIC
- we currently do not have a logo and do not need one at the moment, happy for the designers to just put the business name on the card using appropriate fonts

Target Market(s)

low cost mobile repairs

Industry/Entity Type

Business

Contact Information for Business Card

attracts customers

Font styles to use
Sans Serif

Colors
0255a3
fbee3d
000000

Requirements
Must have
• (555) 381-7094
• Marcello Treviske
• for lower income target market
Nice to have
• "we save you money"
• Easy to read
Should not have
• nothing comes to mind

```html
<!DOCTYPE html>
<html lang="en">
<head>
<meta charset="utf-8">
<title>M'S Mobile Mechanic – Business Card</title>
<link rel="stylesheet" href="https://fonts.googleapis.com/css2?family=Exo+2:wght@400;700&family=Tinos:wght@700&display=swap">
<style>
  :root {
    --brand-blue: #0255a3;
    --brand-yellow: #fbee3d;
    --brand-black: #000000;
    --stage: #e9e7e3;
    --car-blue-light: #1a64ae;
  }
  * { margin: 0; padding: 0; box-sizing: border-box; }
  html, body {
    width: 1200px;
    height: 800px;
    overflow: hidden;
    background: var(--stage);
  }
  .stage {
    position: relative;
    width: 1200px;
    height: 800px;
    display: flex;
    align-items: center;
    justify-content: center;
    gap: 60px;
  }
  .card {
    position: relative;
    width: 520px;
    height: 297px;
    overflow: hidden;
    box-shadow: 0 6px 18px rgba(0,0,0,0.18);
  }

  /* Back of card: business name */
  .card-back {
    background: var(--brand-black);
    display: flex;
    align-items: center;
    justify-content: center;
  }
  .business-name {
    font-family: 'Exo 2', sans-serif;
    font-weight: 700;
    font-size: 34px;
    line-height: 1;
    letter-spacing: 1px;
    color: var(--brand-yellow);
    text-align: center;
    white-space: nowrap;
  }

  /* Front of card: contact */
  .card-front {
    background: var(--brand-blue);
  }
  .contact {
    position: absolute;
    top: 44px;
    left: 0;
    right: 0;
    text-align: center;
  }
  .person-name {
    font-family: 'Exo 2', sans-serif;
    font-weight: 700;
    font-size: 40px;
    color: var(--brand-yellow);
    letter-spacing: 1px;
  }
  .phone-row {
    margin-top: 6px;
    display: flex;
    align-items: center;
    justify-content: center;
    gap: 16px;
  }
  .phone-rule {
    width: 64px;
    height: 2px;
    background: var(--brand-yellow);
  }
  .phone {
    font-family: 'Exo 2', sans-serif;
    font-weight: 400;
    font-size: 24px;
    color: var(--brand-yellow);
    letter-spacing: 1px;
  }
  .footer-band {
    position: absolute;
    left: 0;
    bottom: 0;
    width: 520px;
    height: 92px;
  }
  .slogan {
    position: absolute;
    left: 30px;
    bottom: 36px;
    font-family: 'Tinos', serif;
    font-weight: 700;
    font-size: 17px;
    color: var(--brand-blue);
    letter-spacing: 0.5px;
    text-transform: uppercase;
  }
</style>
</head>
<body>
<main class="stage">

  <section class="card card-back" aria-label="Business card back">
    <h1 class="business-name">M'S MOBILE MECHANIC</h1>
  </section>

  <section class="card card-front" aria-label="Business card front">
    <div class="contact">
      <h2 class="person-name">Marcello Treviske</h2>
      <div class="phone-row">
        <span class="phone-rule"></span>
        <span class="phone">(555) 381-7094</span>
        <span class="phone-rule"></span>
      </div>
    </div>

    <svg class="footer-band" viewBox="0 0 520 92">
      <defs>
        <linearGradient id="car-area" x1="0" y1="0" x2="1" y2="0">
          <stop offset="0" stop-color="#0255a3"/>
          <stop offset="1" stop-color="#1a64ae"/>
        </linearGradient>
      </defs>
      <rect x="0" y="0" width="520" height="92" fill="#fbee3d"/>
      <path d="M285 92 L300 40 Q305 30 318 28 L520 22 L520 92 Z"
            fill="url(#car-area)" role="img"
            aria-label="Yellow line illustration of a car in side view"/>
    </svg>
    <p class="slogan">We save you money</p>
  </section>

</main>
</body>
</html>
```